Create a memorable Web Design for real estate branding

we are a Minnepolis brokerage and boutique housing specialist with over 27 years of experience in the Global furnished housing industry, servicing the Greater Los Angeles area. Specializing in “warm environments” we offer a customized approach to satisfying our guests and client’s needs by offering a wide array of options in highly desirable areas. Additionally, Lanterly Homes Collective offers assistance and expertise to home buyers, sellers and investors.

Industry/Entity Type

Real Estate

Number of Pages Required

1 page

Font styles to use
Serif
Sans Serif
Decorative

```html
<!DOCTYPE html>
<html lang="en">
<head>
<meta charset="utf-8">
<title>Lanterly Homes Collective</title>
<link rel="stylesheet" href="https://fonts.googleapis.com/css2?family=Arimo:ital,wght@0,400;0,700;1,400;1,700&family=Tinos&display=swap">
<style>
:root{
  --teal:#16a58c;
  --green:#8dc63f;
  --green-band:#9cc83c;
  --ink:#333;
  --line:#d6d6d6;
  --white:#fff;
  --hero-top:#9dbbdc;
  --hero-bottom:#8e948a;
  --listing-bg:#4b4540;
  --card-photo:#1a2230;
  --portrait:#c9cfd5;
}
*{box-sizing:border-box;margin:0;padding:0}
html,body{width:793px;height:1200px;overflow:hidden;background:var(--white)}
body{position:relative;font-family:Arimo,Arial,sans-serif;color:var(--ink)}

/* header */
.brand{position:absolute;left:76px;top:16px;line-height:1}
.brand-name{display:block;font-size:17px;font-weight:700;color:var(--teal)}
.brand-sub{display:block;font-size:11px;font-weight:700;color:var(--teal);margin-top:3px;letter-spacing:.5px}
.nav{position:absolute;top:30px;left:0;width:793px;font-size:8.5px;letter-spacing:.6px}
.nav a{position:absolute;color:var(--ink);text-decoration:none}
.nav a.active{color:var(--green)}

/* hero */
.hero-photo{position:absolute;left:0;top:62px;width:793px;height:430px;
  background:linear-gradient(180deg,var(--hero-top) 0%,var(--hero-bottom) 100%)}
.search-frame{position:absolute;left:54px;top:110px;width:242px;height:292px;background:var(--teal);opacity:.85}
.search{position:absolute;left:66px;top:119px;width:220px;height:274px;background:var(--white)}
.search h1{position:absolute;left:11px;top:26px;font-size:15.5px;font-weight:400;color:var(--ink);white-space:nowrap}
.search h1 em{color:var(--green);font-style:italic}
.field{position:absolute;border:1px solid var(--teal);border-radius:2px;font-size:7.5px;color:var(--teal);padding-left:7px;display:flex;align-items:center;height:25px}
.field.placeholder{color:#9a9a9a;font-style:italic}
.field .caret{position:absolute;right:9px;top:9px;width:0;height:0;border-left:5px solid transparent;border-right:5px solid transparent;border-top:8px solid var(--teal)}
.label{position:absolute;font-size:7.5px;color:var(--ink);width:94px;text-align:center}
.find-btn{position:absolute;left:11px;top:239px;width:198px;height:24px;background:var(--green);color:var(--white);font-size:10px;font-weight:700;display:flex;align-items:center;justify-content:center}

/* quick links */
.band{position:absolute;left:0;top:492px;width:793px;height:76px;background:var(--green-band)}
.quick{position:absolute;top:502px;height:55px;background:var(--white);display:flex;align-items:center;gap:5px;padding-left:9px;color:var(--green);font-size:14px;line-height:1.05}
.quick.small{font-size:10.5px;font-weight:700}
.quick svg{flex:none}

/* about */
.about-photo{position:absolute;left:55px;top:579px;width:270px;height:280px;border:1px solid var(--teal);background:var(--portrait)}
.about h2{position:absolute;left:334px;top:586px;white-space:nowrap;font-size:26px;font-weight:700;color:var(--teal)}
.about h2 .sub{font-family:Tinos,'Times New Roman',serif;font-weight:400;font-size:20px;color:var(--green)}
.about-copy{position:absolute;left:338px;top:632px;width:390px;font-size:8.3px;line-height:14.1px;color:var(--ink)}
.about-copy p{margin-bottom:14px}

/* listings */
.listings-bg{position:absolute;left:0;top:871px;width:793px;height:173px;background:var(--listing-bg)}
.listings-panel{position:absolute;left:46px;top:883px;width:700px;height:149px;background:var(--teal);opacity:.9}
.card{position:absolute;top:891px;width:120px;height:130px;background:var(--white);border-top:3px solid var(--white)}
.card-photo{height:77px;background:var(--card-photo)}
.card p{font-size:7.6px;line-height:9.5px;color:#111;padding:3px 5px 0}
.details{position:absolute;left:32px;bottom:7px;width:56px;height:17px;border:1px solid #777;font-size:7px;color:#666;display:flex;align-items:center;justify-content:center;gap:5px}
.arrow{position:absolute;top:942px}

/* footer */
.footer-links{position:absolute;top:1105px;font-size:8px;color:var(--ink);white-space:nowrap}
.footer-links span{padding:0 3px;color:#999}
.legal{position:absolute;left:66px;top:1146px;font-size:7.5px;line-height:10px;color:var(--ink)}
.divider{position:absolute;top:1092px;width:1px;height:86px;background:var(--line)}
.footer-brand{position:absolute;left:328px;top:1114px;line-height:1;text-align:right;width:162px}
.footer-brand .brand-name{font-size:16px}
.footer-brand .brand-sub{font-size:12px}
.expertise{position:absolute;left:565px;top:1105px;font-size:8px;color:var(--ink)}
.social{position:absolute;top:1152px;width:23px;height:23px;background:var(--green)}
</style>
</head>
<body>

<header>
  <div class="brand"><span class="brand-name">Lanterly Homes</span><span class="brand-sub">COLLECTIVE</span></div>
  <nav class="nav">
    <a class="active" style="left:358px">BUY</a>
    <a style="left:419px">SELL</a>
    <a style="left:480px">RENT</a>
    <a style="left:541px">SERVICES</a>
    <a style="left:623px">ABOUT</a>
    <a style="left:684px">CONTACT</a>
  </nav>
</header>

<section class="hero">
  <div class="hero-photo" role="img" aria-label="Photo of a suburban street with large family homes"></div>
  <div class="search-frame"></div>
  <form class="search">
    <h1>FIND YOUR <em>DREAM HOME</em></h1>
    <div class="field" style="left:11px;top:72px;width:198px">Find <i>&nbsp;ZIP Code...</i><span class="caret"></span></div>
    <div class="field" style="left:11px;top:106px;width:198px">Property Type<span class="caret"></span></div>
    <div class="label" style="left:11px;top:139px">BEDS</div>
    <div class="label" style="left:115px;top:139px">BATHS</div>
    <div class="field placeholder" style="left:11px;top:151px;width:94px">No. of Beds ...</div>
    <div class="field placeholder" style="left:115px;top:151px;width:94px">No. of Bathroom..</div>
    <div class="label" style="left:11px;top:184px">MAX PRICE</div>
    <div class="label" style="left:115px;top:184px">MIN PRICE</div>
    <div class="field placeholder" style="left:11px;top:196px;width:94px">Max price...</div>
    <div class="field placeholder" style="left:115px;top:196px;width:94px">Min price...</div>
    <div class="find-btn">FIND PROPERTY</div>
  </form>
</section>

<section class="quick-links">
  <div class="band"></div>
  <div class="quick" style="left:74px;width:120px">
    <svg width="21" height="21" viewBox="0 0 22 22" fill="none" stroke="#8dc63f" stroke-width="1.8"><circle cx="11" cy="11" r="9.5"/><path d="M8 8.5a3 3 0 1 1 4 2.8c-.8.4-1 1-1 2"/><circle cx="11" cy="16" r=".6" fill="#8dc63f"/></svg>INQUIRIES</div>
  <div class="quick" style="left:205px;width:120px">
    <svg width="20" height="22" viewBox="0 0 20 22" fill="none" stroke="#8dc63f" stroke-width="1.8"><path d="M2 10 10 2l8 8v10H2z"/><circle cx="10" cy="12" r="3"/><path d="m12 14 3 3"/></svg>HELP! ME<br>RELOCATE</div>
  <div class="quick small" style="left:336px;width:120px">
    <svg width="22" height="22" viewBox="0 0 22 22" fill="none" stroke="#8dc63f" stroke-width="1.6"><path d="M3 11 11 3l8 8"/><path d="M5 9v10h12V9"/><circle cx="11" cy="13" r="3"/></svg>WHAT MY<br>HOME WORTH?</div>
  <div class="quick" style="left:467px;width:120px;padding-left:20px">
    <svg width="26" height="22" viewBox="0 0 26 22" fill="none" stroke="#8dc63f" stroke-width="1.8"><path d="M9 2h14v18H9"/><path d="M2 11h14M12 7l4 4-4 4"/></svg>LOGIN</div>
  <div class="quick" style="left:599px;width:115px;padding-left:8px">
    <svg width="26" height="24" viewBox="0 0 26 24" fill="none" stroke="#8dc63f" stroke-width="1.8"><path d="M16 3H3v19h13"/><path d="M9 18l2-5 11-11 3 3-11 11z"/></svg>REGISTER</div>
</section>

<section class="about">
  <div class="about-photo" role="img" aria-label="Portrait photo of the lead real estate agent"></div>
  <h2><span style="color:var(--teal)">Lanterly</span> <span style="color:var(--green)">Homes</span> <span class="sub">Collective</span></h2>
  <div class="about-copy">
    <p>Lorem ipsum dolor sit amet, consectetuer adipiscing elit. Aenean commodo ligula eget dolor. Aenean massa. Cum sociis natoque penatibus et magnis dis parturient montes, nascetur ridiculus mus. Donec quam felis, ultricies nec, pellentesque eu, pretium quis, sem. Nulla consequat massa quis enim. Donec pede justo, fringilla vel, aliquet nec, vulputate eget, arcu. In enim justo, rhoncus ut, imperdiet a, venenatis vitae, justo. Nullam dictum felis eu pede mollis pretium. Integer tincidunt.</p>
    <p>Cras dapibus. Vivamus elementum semper nisi. Aenean vulputate eleifend tellus. Aenean leo Lorem ipsum dolor sit amet, consectetuer adipiscing elit. Aenean commodo ligula eget dolor. Aenean massa. Cum sociis natoque penatibus et magnis dis parturient montes, nascetur ridiculus mus. Donec quam felis, ultricies nec, pellentesque eu, pretium quis, sem. Nulla consequat massa quis enim. Donec pede justo, fringilla vel, aliquet nec, vulputate eget, arcu. In enim justo, rhoncus ut, imperdiet a, venenatis vitae, justo. Nullam dictum felis eu pede mollis pretium. Integer tincidunt</p>
    <p>venenatis vitae, justo. Nullam dictum felis eu pede mollis pretium. Integer tincidunt<br>venenatis vitae, justo. Nullam dictum felis eu pede mollis pretium. Integer tincidunt asdad<br>venenatis vitae, justo. Nullam dictum felis eu.</p>
  </div>
</section>

<section class="listings">
  <div class="listings-bg" role="img" aria-label="Background photo of a town street"></div>
  <div class="listings-panel"></div>
  <svg class="arrow" style="left:50px" width="16" height="34" viewBox="0 0 16 34" fill="none" stroke="#fff" stroke-width="1.5"><path d="M15 1 1 17l14 16"/></svg>
  <svg class="arrow" style="left:727px" width="16" height="34" viewBox="0 0 16 34" fill="none" stroke="#fff" stroke-width="1.5"><path d="m1 1 14 16L1 33"/></svg>

  <article class="card" style="left:74px"><div class="card-photo" role="img" aria-label="Photo of a listed property"></div><p>Lorem ipsum dolor sit amet, consectetuer adipiscing elit.</p><div class="details"><svg width="9" height="8" viewBox="0 0 9 8" fill="none" stroke="#777"><rect x=".5" y=".5" width="8" height="7"/><path d="M4.5 2v4M2.5 4h4"/></svg>DETAILS</div></article>
  <article class="card" style="left:205px"><div class="card-photo" role="img" aria-label="Photo of a listed property"></div><p>Lorem ipsum dolor sit amet, consectetuer adipiscing elit.</p><div class="details"><svg width="9" height="8" viewBox="0 0 9 8" fill="none" stroke="#777"><rect x=".5" y=".5" width="8" height="7"/><path d="M4.5 2v4M2.5 4h4"/></svg>DETAILS</div></article>
  <article class="card" style="left:337px"><div class="card-photo" role="img" aria-label="Photo of a listed property"></div><p>Lorem ipsum dolor sit amet, consectetuer adipiscing elit.</p><div class="details"><svg width="9" height="8" viewBox="0 0 9 8" fill="none" stroke="#777"><rect x=".5" y=".5" width="8" height="7"/><path d="M4.5 2v4M2.5 4h4"/></svg>DETAILS</div></article>
  <article class="card" style="left:468px"><div class="card-photo" role="img" aria-label="Photo of a listed property"></div><p>Lorem ipsum dolor sit amet, consectetuer adipiscing elit.</p><div class="details"><svg width="9" height="8" viewBox="0 0 9 8" fill="none" stroke="#777"><rect x=".5" y=".5" width="8" height="7"/><path d="M4.5 2v4M2.5 4h4"/></svg>DETAILS</div></article>
  <article class="card" style="left:599px"><div class="card-photo" role="img" aria-label="Photo of a listed property"></div><p>Lorem ipsum dolor sit amet, consectetuer adipiscing elit.</p><div class="details"><svg width="9" height="8" viewBox="0 0 9 8" fill="none" stroke="#777"><rect x=".5" y=".5" width="8" height="7"/><path d="M4.5 2v4M2.5 4h4"/></svg>DETAILS</div></article>
</section>

<footer>
  <div class="footer-links" style="left:66px">BUY<span>|</span>SELL<span>|</span>RENT<span>|</span>SERVICES<span>|</span>ABOUT<span>|</span>CONTACT</div>
  <div class="legal">Copyright © 2016 lanterlyhomes.example All rights reserved.<br>Sitemap | Real Estate Web Marketing by Parcel Web Studio</div>
  <div class="divider" style="left:301px"></div>
  <div class="footer-brand"><span class="brand-name">Lanterly Homes</span><span class="brand-sub">COLLECTIVE</span></div>
  <div class="divider" style="left:516px"></div>
  <div class="expertise">AREAS OF EXPERTISE</div>
  <div class="footer-links" style="left:528px;top:1124px;line-height:10px">INQUIRIES<span>|</span>HELP! ME RELOCATE<span>|</span>WHAT<br>MY HOME WORTH?</div>
  <div class="social" style="left:619px" aria-label="Social link"></div>
  <div class="social" style="left:647px" aria-label="Social link"></div>
  <div class="social" style="left:675px" aria-label="Social link"></div>
</footer>

</body>
</html>
```